Mossy Den Pet Supply

Thank you for your interest in this design contest. We are always welcome to questions and are looking forward to seeing what you can come up with.

We work on a Bootstrap platform with our custom built CMS. We require all designs to be sized accordingly with the bootstrap grid system found here: http://fernlattice.com/css/#grid

At the start of a competition, we are looking for general Home Page Design concepts and an example product grid page.

Homepage: Slide Show/Featured Products/Specials

example website as a reference:https://www.mintcollarworks.com/

Store Product Grid: Show a grid of product thumbnails. Included elements are thumbnail and price. Also included are filters (sort by, show by grid/list).

No photos at this time but Logo is attached. Looking for good quality photo's around the web. Please read the attached creative brief in depth to get an idea f what the client is looking for. Thanks!

```html
<!DOCTYPE html>
<html lang="en">
<head>
<meta charset="utf-8">
<title>Mossy Den Pet Supply</title>
<link rel="stylesheet" href="https://fonts.googleapis.com/css2?family=Roboto:wght@300;400;700&family=Roboto+Condensed:wght@400&family=Open+Sans:wght@400&display=swap">
<style>
  :root{
    --purple:#650c5f;
    --green:#7dc242;
    --green-deep:#3fa535;
    --hero-a:#3aa537;
    --hero-b:#82c341;
    --ink:#111;
    --white:#fff;
    --line:#222;
  }
  *{box-sizing:border-box;margin:0;padding:0}
  html,body{width:1200px;height:900px;overflow:hidden;background:var(--white);font-family:"Roboto",Arial,sans-serif;color:var(--ink)}
  .page{position:relative;width:1200px;height:900px;overflow:hidden}

  .brand{position:absolute;left:150px;top:96px;width:115px;text-align:center;font-weight:700;font-size:17px;line-height:20px;color:#2a2a2a;letter-spacing:.5px}
  .brand-mark{display:block;width:14px;height:14px;background:#2a2a2a;margin:0 auto 8px}

  .main-nav{position:absolute;left:281px;top:123px;width:391px;height:35px;background:var(--purple);font-size:13px;color:var(--white)}
  .main-nav span{position:absolute;top:10px}
  .caret{font-size:8px;top:12px!important}

  .search{position:absolute;left:705px;top:130px;width:248px;height:24px;border:1px solid var(--purple)}
  .search-label{position:absolute;left:37px;top:4px;font-size:11px;font-style:italic;color:#888}
  .search svg{position:absolute;right:3px;top:2px}

  .cart{position:absolute;left:984px;top:0;width:78px;height:63px;background:var(--green);color:var(--white);text-align:center}
  .cart-icon{position:absolute;left:37px;top:18px;width:26px;height:26px;border-radius:50%;background:var(--purple)}
  .cart-icon svg{position:absolute;left:6px;top:6px}
  .cart-label{position:absolute;left:0;right:0;top:47px;font-size:11px}
  .cart-total{position:absolute;right:143px;top:66px;text-align:right;font-size:12px;line-height:12px}
  .cart-total small{display:block;font-size:8px;line-height:10px}
  .cart-total a{display:block;font-size:8px;color:var(--purple);text-decoration:none;line-height:14px}
  .login{position:absolute;left:984px;top:105px;width:78px;height:19px;background:var(--green);color:var(--white);font-size:10px;text-align:center;line-height:19px}
  .social{position:absolute;top:129px;width:23px;height:23px;background:var(--green)}

  .hero{position:absolute;left:126px;top:158px;width:936px;height:513px;background:linear-gradient(135deg,var(--hero-a),var(--hero-b))}
  .hero-photo{position:absolute;left:390px;top:22px;width:546px;height:491px;background:radial-gradient(ellipse at 55% 55%,#f4f2ee 0%,#d9d2c6 45%,rgba(60,40,30,.55) 75%,rgba(130,195,65,0) 90%)}
  .hero-panel{position:absolute;left:0;top:161px;width:390px;height:146px;background:var(--white)}
  .hero-title{position:absolute;left:83px;top:6px;font-weight:300;font-size:47px;line-height:48px;color:var(--ink)}
  .hero-title .line3{font-size:38px;line-height:44px}
  .hero-title .tag{background:var(--purple);color:var(--white);padding:0 16px 0 12px}
  .hero-cta{position:absolute;left:312px;top:325px;width:78px;height:43px;background:var(--purple);color:var(--white);font-family:"Roboto Condensed",Arial,sans-serif;font-size:15px;line-height:17px;text-align:center;padding-top:4px}
  .dots{position:absolute;left:84px;top:487px;display:flex;gap:4px}
  .dots i{width:19px;height:19px;border-radius:50%;border:3px solid var(--white)}
  .dots i.on{background:var(--purple)}

  .tabs{position:absolute;top:698px;left:332px;height:33px;font-size:21px;line-height:33px;white-space:nowrap}
  .tabs span{position:absolute;top:0}
  .tab-active{background:var(--green-deep);color:var(--white);padding:0 12px;width:133px}

  .card{position:absolute;top:749px;width:189px;height:170px;border:1px solid var(--line);overflow:hidden}
  .card.hot{background:var(--green-deep)}
  .card-img{position:absolute;left:18px;top:16px;width:150px;height:112px;border-radius:40%}
  .card-text{padding:7px 8px;font-family:"Open Sans",Arial,sans-serif;font-size:11.4px;line-height:14.6px;color:var(--white)}
  .card-name{position:absolute;left:8px;top:141px;font-size:17px;font-weight:300}
  .hot .card-name{color:var(--ink)}
  .card-add{position:absolute;right:6px;top:144px;width:34px;height:34px;border-radius:50%;background:var(--purple)}
</style>
</head>
<body>
<div class="page">
  <div class="brand"><span class="brand-mark"></span>MOSSY DEN<br>PET SUPPLY</div>

  <nav class="main-nav">
    <span style="left:24px">BLOG</span>
    <span style="left:102px">SHOP</span>
    <span class="caret" style="left:149px">▼</span>
    <span style="left:165px">GALLERIES</span><span class="caret" style="left:228px">▼</span>
    <span style="left:257px">NEWS</span>
    <span style="left:325px">CONTACT</span>
  </nav>

  <div class="search">
    <span class="search-label">search</span>
    <svg width="18" height="18" viewBox="0 0 18 18"><circle cx="7" cy="7" r="5" fill="none" stroke="#650c5f" stroke-width="2"/><line x1="11" y1="11" x2="16" y2="16" stroke="#650c5f" stroke-width="3"/></svg>
  </div>

  <div class="cart">
    <div class="cart-icon"><svg width="14" height="14" viewBox="0 0 14 14"><path d="M1 2h2l2 7h6l2-5H4" fill="none" stroke="#fff" stroke-width="1.4"/><circle cx="6" cy="12" r="1.2" fill="#fff"/><circle cx="10" cy="12" r="1.2" fill="#fff"/></svg></div>
    <div class="cart-label">YOUR CART</div>
  </div>
  <div class="cart-total">$788.99<small>(6 products)</small><a>see cart / confirm</a></div>
  <div class="login">login / register</div>
  <div class="social" style="left:999px"></div>
  <div class="social" style="left:1025px"></div>

  <section class="hero">
    <div class="hero-photo" role="img" aria-label="Photo of a white, black and tan terrier puppy looking toward the viewer"></div>
    <div class="hero-panel">
      <div class="hero-title">ALL FOR<br>YOUR <span class="tag">DOG</span><br><span class="line3">AT ONE PLACE</span></div>
    </div>
    <div class="hero-cta">SEE OUR<br>SELECTION</div>
    <div class="dots"><i class="on"></i><i></i><i></i></div>
  </section>

  <div class="tabs">
    <span class="tab-active" style="left:0">FEATURED</span>
    <span style="left:138px">|</span>
    <span style="left:162px">BEST SELLERS</span>
    <span style="left:330px">|</span>
    <span style="left:354px">NEW PRODUCTS</span>
  </div>

  <div class="card" style="left:158px">
    <div class="card-img" role="img" aria-label="Photo of a dark rubber bone chew toy" style="background:radial-gradient(ellipse,#3a3a3a 0%,#777 40%,#fff 70%)"></div>
    <div class="card-name">Product 1</div><div class="card-add"></div>
  </div>
  <div class="card hot" style="left:385px">
    <p class="card-text">Cum sociis natoque penatibus et magnis dis parturient montes, nascetur ridiculus mus. Interdum et malesuada fames ac ante ipsum primis in faucibus. Mauris vitae lorem eget nulla pretium luctus quis nec urna. Fusce phare-tra iaculis mauris, sed consectetur</p>
    <div class="card-name">Product 1</div><div class="card-add"></div>
  </div>
  <div class="card" style="left:613px">
    <div class="card-img" role="img" aria-label="Photo of a fluffy pink plush dog toy" style="background:radial-gradient(ellipse,#e8329a 0%,#f27cc0 40%,#fff 70%)"></div>
    <div class="card-name">Product 1</div><div class="card-add"></div>
  </div>
  <div class="card" style="left:842px">
    <div class="card-img" role="img" aria-label="Photo of a lime green twisted chew toy" style="background:radial-gradient(ellipse,#b9d83a 0%,#d6ea7c 40%,#fff 70%)"></div>
    <div class="card-name">Product 1</div><div class="card-add"></div>
  </div>
</div>
</body>
</html>
```